Inspiring book cover design (business book for designers and innovators)

I'm writing my first book, to be published early next year. I'm struggling to come up with an inspiring book cover design. I need your help!

Information to be included on the cover:
Book Title: Bright maker's manual
Subtitle: Designing products and services that make sense
Author: Marianne Colt
Optional (not sure yet if I should include this on the cover): with online toolset

The book will be a square, size 170 x 170 mm
In the uploaded file you can find some example pages from the inside of the book. The cover design should fit with the design style of the example pages. The cover should "jump out" from the shelve in a bookstore and should attract designers, innovators, product managers, developers, and startup founders to buy the book.
Publisher: www.quillmarkpress.example

About the book:
Why do some products fail while others become a success? Why do so many companies launch crappy products and services that nobody wants? This book is both a guide to and a source of inspiration for, designing products and services that make sense. Because if they make sense to people, people will want them.
In order for tech products and services to make sense, and create value for users, we need to apply technologies in a meaningful way. We can achieve this by designing strong benefits and at the same time minimizing resistance users might have against new technologies.
This book offers a complete overview of how to develop products and services that make sense: 27 ways to strengthen benefits and 28 ways to mitigate resistance. It offers practical insights, examples, tips, and tools to design products and services that people will love to use.

About the author:
https://www.linkedin.example/in/mariannecolt/

Target Market(s)

designers, innovators, product managers, developers, and startup founders

Industry/Entity Type

Design Agency

Font styles to use
Other font styles liked:
• You can choose. The inside of the book uses 3 fonts: LuloCleanW01-OneBold, Sansation, Segoe UI

Requirements
Must have
• Clean, yet creative design.
Square shape
Fits the design style of the example pages
Sans serif fonts. Do not have to be the same fonts like the ones that are used inside the book (LuloCleanW01-OneBold, Sansation, Segoe UI), but should go well with them.

Bright makers manual
48 ways to build solutions and platforms that feel right
Marianne Colt
Nice to have
• I have several ideas that you might take as a starting point:
1) Do something with the left brain (rational, more digital) - right brain (creative, more emotional). For products to make sense, it needs to appeal to both parts of the brain
2) Work with a pattern, for example a (polygonal) triangular pattern
3) playful element in the letters, for example turning the O in innovator's into an on-off button or a stylish smiley, flipping the N in innovator's, doing something playful with the ' in innovator's
I've uploaded some images as a source of inspiration.

The cover should have a different color than the red/blue used in the example pages, but should fit the color palette that is used in the example pages.
Trigger curiosity.
Should not have
• Photographic pictures

```html
<!DOCTYPE html>
<html lang="en">
<head>
<meta charset="utf-8">
<title>Bright Maker's Manual – Book Cover</title>
<link rel="stylesheet" href="https://fonts.googleapis.com/css2?family=Oswald:wght@700&family=Arimo:wght@700&display=swap">
<style>
  :root {
    --backdrop: #bdbdbd;
    --crimson: #9c1532;
    --crimson-deep: #7a1030;
    --plum: #4a1030;
    --midnight: #120d2e;
    --ink: #05051a;
    --paper: #ffffff;
    --glow-amber: #f0a24a;
    --glow-rose: #d86a9a;
    --glow-cyan: #5fd6ee;
  }
  html, body {
    margin: 0;
    padding: 0;
    width: 1200px;
    height: 1160px;
    overflow: hidden;
    background: var(--backdrop);
  }
  .cover {
    position: absolute;
    left: 122px;
    top: 103px;
    width: 955px;
    height: 955px;
    overflow: hidden;
    background:
      linear-gradient(168deg, var(--crimson) 0%, var(--crimson-deep) 35%, var(--plum) 58%, var(--midnight) 78%, var(--ink) 100%);
  }
  .cover__pattern {
    position: absolute;
    inset: 0;
    background:
      radial-gradient(ellipse 60% 40% at 95% 10%, rgba(170, 25, 50, 0.55), transparent 70%),
      radial-gradient(ellipse 55% 45% at 10% 30%, rgba(160, 20, 50, 0.45), transparent 70%);
  }
  .cover__art {
    position: absolute;
    left: 367px;
    top: 335px;
    width: 500px;
    height: 440px;
    border-radius: 50% 46% 40% 48% / 48% 52% 45% 50%;
    background:
      radial-gradient(circle at 35% 42%, rgba(255, 230, 200, 0.95) 0%, var(--glow-amber) 12%, transparent 32%),
      radial-gradient(circle at 52% 30%, var(--glow-rose) 0%, transparent 38%),
      radial-gradient(circle at 72% 58%, rgba(220, 250, 255, 0.95) 0%, var(--glow-cyan) 14%, transparent 38%),
      radial-gradient(ellipse at 55% 50%, rgba(90, 60, 140, 0.6) 0%, transparent 75%);
    opacity: 0.9;
  }
  .cover__title {
    position: absolute;
    left: 55px;
    top: 42px;
    margin: 0;
    font-family: "Oswald", "Arial Narrow", sans-serif;
    font-weight: 700;
    font-size: 100px;
    line-height: 114px;
    letter-spacing: 0.5px;
    text-transform: uppercase;
    color: var(--paper);
  }
  .cover__title span { display: block; }
  .cover__subtitle {
    position: absolute;
    left: 54px;
    top: 555px;
    margin: 0;
    font-family: "Arimo", "Helvetica Neue", Arial, sans-serif;
    font-weight: 700;
    font-size: 36px;
    line-height: 45.5px;
    text-transform: uppercase;
    color: var(--paper);
  }
  .cover__subtitle span { display: block; }
  .cover__author-band {
    position: absolute;
    left: 0;
    top: 822px;
    width: 955px;
    height: 92px;
    background:
      radial-gradient(ellipse 180px 90px at 15% 100%, rgba(30, 5, 15, 0.85), transparent 80%),
      linear-gradient(90deg, var(--plum) 0%, var(--crimson) 40%, var(--crimson) 100%);
  }
  .cover__author {
    position: absolute;
    right: 34px;
    top: 0;
    margin: 0;
    font-family: "Oswald", "Arial Narrow", sans-serif;
    font-weight: 700;
    font-size: 55px;
    line-height: 92px;
    text-transform: uppercase;
    color: var(--paper);
  }
  .cover__foot {
    position: absolute;
    left: 0;
    top: 914px;
    width: 955px;
    height: 41px;
    background: var(--ink);
  }
</style>
</head>
<body>
  <main class="cover">
    <div class="cover__pattern" role="img" aria-label="Faceted triangular polygon pattern in crimson fading to deep midnight blue"></div>
    <div class="cover__art" role="img" aria-label="Illustration of a brain outline made of connected glowing nodes over a colourful starry nebula"></div>
    <h1 class="cover__title">
      <span>Bright</span>
      <span>Maker's</span>
      <span>Manual</span>
    </h1>
    <p class="cover__subtitle">
      <span>48 ways to</span>
      <span>build solutions</span>
      <span>and platforms</span>
      <span>that feel right</span>
    </p>
    <div class="cover__author-band">
      <p class="cover__author">Marianne Colt</p>
    </div>
    <div class="cover__foot"></div>
  </main>
</body>
</html>
```